Consulting Firm stationery design

Now that the ArtHive has given us a new logo we'll now need to have all our stationery designed. So we're asking for this community to help us once again.We're looking to get from you Letterheads (Header and Footer, suitable to be applied on a .docx format. Vectors are required but keep this in mind), Envelopes (Front and Back designs, back is not a must but desirable depending on your design), 9"x 12" Pocket Folders (consider design for front and back, also for pockets as well), Business Cards.An elegant design is a must have, mostly for Folders and Envelopes. The idea with this two is to stand out from others when they're handed over. Ideas are welcomed, we were thinking maybe on some texturing simulation for these.Folders will have 3 addresses and contact information. Envelopes will have 1 address and contact information.Brand Manual attached. marquesino logo has been copyrighted already. I'm also attaching the current stationary designs (these never got to be out for production but was going to be before we made the brand changes); Pocker folders page 1 to 4 (pages 2 and 4 are the pocket designs), Pages 5 and 6 (6 is the back of the envelope), Pages 7 and 8 (8 is the back of the business card). No letterhead within these designs as it just had the logo and address.

Industry/Entity Type

Business Consultant

Font styles to use
Serif
Sans Serif

Requirements
Must have
• Elegance
Nice to have
• Modern looking out of common

```html
<!DOCTYPE html>
<html lang="en">
<head>
<meta charset="UTF-8">
<title>Letterhead Design — marquesino</title>
<link rel="stylesheet" href="https://fonts.googleapis.com/css2?family=Montserrat:wght@300;400;600;700&display=swap">
<style>
  :root {
    --ink: #1d1d1f;
    --brand-dark: #33333f;
    --brand-blue: #1a7fc1;
    --hatch-blue: #9cc3e6;
    --frame: #8a8a8a;
    --paper: #ffffff;
    --body-text: #232323;
  }
  * { margin: 0; padding: 0; box-sizing: border-box; }
  html, body {
    width: 968px; height: 1200px; overflow: hidden;
    background: var(--paper);
    font-family: "Montserrat", sans-serif;
  }
  .canvas { position: relative; width: 968px; height: 1200px; }
  .section-title {
    position: absolute; left: 39px; top: 40px;
    font-size: 26px; font-weight: 700; letter-spacing: 0.2px; color: var(--ink);
  }
  .letter-sheet {
    position: absolute; left: 129px; top: 186px; width: 703px; height: 911px;
    border: 1px solid var(--frame); background: var(--paper);
  }
  .brand-mark {
    position: absolute; left: 93px; top: 70px;
    display: flex; align-items: center; gap: 6px;
  }
  .brand-name {
    font-size: 24px; font-weight: 700; color: var(--brand-dark); letter-spacing: -0.3px;
  }
  .brand-dot {
    width: 11px; height: 11px; border-radius: 50%; background: var(--brand-blue);
  }
  .letter-date, .salutation, .letter-body, .sign-off {
    position: absolute; font-size: 11.7px; font-weight: 400; color: var(--body-text);
  }
  .letter-date { right: 96px; top: 212px; }
  .salutation { left: 96px; top: 231px; }
  .letter-body { left: 96px; top: 286px; width: 511px; line-height: 18.4px; }
  .letter-body p { text-align: justify; margin-bottom: 18.6px; }
  .sign-off { left: 96px; top: 580px; line-height: 19px; }
  .contact-footer {
    position: absolute; left: 47px; top: 789px;
    border-left: 3px solid var(--ink);
    height: 59px; padding-left: 8px; padding-top: 8px;
    display: flex; gap: 31px;
    font-size: 9.3px; line-height: 11.2px; color: var(--body-text); font-weight: 400;
  }
  .office-title { font-weight: 700; }
  .contact-lines { padding-top: 11.2px; }
  .contact-lines b { font-weight: 700; }
  .hatch-band {
    position: absolute; left: 0; bottom: 0; width: 100%; height: 34px;
    background: var(--hatch-blue);
  }
</style>
</head>
<body>
<main class="canvas">
  <h1 class="section-title">LETTERHEAD DESIGN</h1>

  <article class="letter-sheet">
    <header class="brand-mark">
      <span class="brand-name">marquesino</span>
      <span class="brand-dot"></span>
    </header>

    <p class="letter-date">22 July , 2019</p>
    <p class="salutation">Dear Full Name,</p>

    <section class="letter-body">
      <p>Lorem ipsum dolor sit amet, consectetuer adipiscing elit, sed diam nonummy nibh euis&shy;mod tincidunt ut laoreet dolore magna aliquam erat volutpat. Ut wisi enim ad minim veniam, quis nostrud exerci tation ullamcorper suscipit lobortis nisl ut aliquip ex ea com&shy;modo consequat. Duis autem vel eum iriure dolor in hendrerit in vulputate velit esse molestie consequat, vel illum dolore eu feugiat nulla facilisis at vero eros et accumsan et iusto odio dignissim qui blandit praesent luptatum zzril delenit augue duis dolore te feugait nulla facilisi.</p>
      <p>Lorem ipsum dolor sit amet, consectetuer adipiscing elit, sed diam nonummy nibh euis&shy;mod tincidunt ut laoreet dolore magna aliquam erat volutpat. Ut wisi enim ad minim veniam, quis nostrud exerci tation ullamcorper suscipit lobortis nisl ut aliquip ex ea com&shy;modo consequat. Duis autem vel eum iriure dolor in hendrerit in vulputate velit esse molestie consequat, vel illum dolore eu feugiat nulla facilisis at vero eros et accumsan et iusto odio dignissim qui blandit praesent luptatum zzril delenit.</p>
    </section>

    <p class="sign-off">Sincerely,<br>Name Goes Here</p>

    <footer class="contact-footer">
      <address class="office-address" style="font-style:normal">
        <span class="office-title">Oficina Administrativa</span><br>
        Cedro Business Plaza<br>
        Avenida Los Almendros 42, Naco<br>
        Santo Domingo, Rep. Dominicana
      </address>
      <div class="contact-lines">
        <b>D</b> (809) 555 0147 ext. 310<br>
        <b>M</b> (809) 555 0182<br>
        <b>E</b> contacto@marquesino.do
      </div>
    </footer>

    <div class="hatch-band" role="img" aria-label="Blue diagonal hatch band along the bottom edge"></div>
  </article>
</main>
</body>
</html>
```